New webpage design for Varplen.se, participant management system informationpage.

Project Brief: New Website Design for Varplen.se (Participant Management System)
About Varplen.se:
Varplen.se is an established participant management system used by organizations and course providers in Sweden to handle event and course registrations. Our website’s primary audience is course providers, event organizers, and potential users seeking efficient management tools.
Project Goal:
We are launching a new public-facing website for Varplen.se, which will present information about our system, features, FAQ, pricing, news, testimonials, and more. The new site will be built in Umbraco CMS and should follow our visual identity as described in the attached graphic manual.
Deliverables:
We need complete, modern, and responsive page designs (desktop and mobile) for the following pages:
- Home page (landing page)
- Features page
- FAQ page
- About Us page
- Contact Us / Book a Demo page
- Pricing page
- Testimonials page
- News / Blog page
Design Guidelines:
- Please use the attached Lumoxa graphic manual for guidance (Lumoxa is a sister project; use the same branding).
- The Varplen.se logo is attached and must be included.
- Please use the blue color palette variant from the guide.
- Typography and graphic elements should be consistent with the manual.
- Designs must be suitable for implementation in Umbraco CMS (avoid overly complex layouts or animations that might be difficult to develop).
- All designs should be responsive and work well on desktop, tablet, and mobile.
- Final deliverables should be provided in Figma or Adobe XD (preferably Figma).
What We Like:
- Clean, modern, Scandinavian style.
- Clear navigation and strong hierarchy.
- Readable, accessible layouts.
What to Avoid:
- Overly playful or cartoonish elements.
- Too much clutter or excessive graphical elements.
- Dark color schemes (please focus on blue/light).
References:
- Our current site: https://varplen-example.se
- Graphic manual (see attachment)
- Varplen logo (see attachment)
Additional Notes:
- The new design should improve clarity, usability, and visual appeal compared to our current site.
- Feel free to suggest visual improvements, but remain consistent with our brand guidelines.
Other font styles liked:
- Orev and Cabin. See attached font files

```html
<!DOCTYPE html>
<html lang="en">
<head>
<meta charset="utf-8">
<title>Varplen – Manage Your Events & Courses</title>
<link href="https://fonts.googleapis.com/css2?family=Poppins:wght@300;400;500;600&family=Russo+One&display=swap" rel="stylesheet">
<style>
:root{
  --blue:#1ea0dc;
  --blue-soft:#d7ecf8;
  --pink:#e8185a;
  --band:#232a31;
  --card:#3b434b;
  --ink:#1a1a1a;
  --muted:#444;
  --line:#d9d9d9;
  --grey-band:#ececec;
  --yellow:#f0b429;
  --teal:#1c9a86;
  --rose:#e83e74;
  --footer:#1f2429;
}
*{box-sizing:border-box;margin:0;padding:0}
html,body{width:1200px;height:3623px;overflow:hidden}
body{position:relative;font-family:"Poppins",sans-serif;color:var(--ink);background:#fff}
.abs{position:absolute}
.display{font-family:"Russo One",sans-serif;font-weight:400}
.shapes{position:absolute;left:0;top:0;width:1200px;height:3623px;z-index:0}
section,header,footer,.layer{position:absolute;left:0;width:1200px;z-index:1}

/* hero */
.hero-photo{position:absolute;left:0;top:0;width:1200px;height:720px;z-index:0;
  clip-path:polygon(0 0,100% 0,100% 640px,0 718px);
  background:
    radial-gradient(ellipse 420px 300px at 880px 300px,rgba(120,160,190,.55),rgba(120,160,190,0) 70%),
    radial-gradient(ellipse 380px 420px at 1120px 180px,rgba(190,160,130,.5),rgba(190,160,130,0) 70%),
    linear-gradient(100deg,#2b3540 0%,#3d4a56 45%,#56636e 100%)}
.hero-photo::after{content:"";position:absolute;inset:0;background:linear-gradient(90deg,rgba(18,24,30,.55) 0%,rgba(18,24,30,.2) 55%,rgba(18,24,30,0) 100%)}
.nav{top:18px;height:40px}
.logo{position:absolute;left:75px;top:0;font-weight:300;font-size:40px;letter-spacing:1px;color:#fff;line-height:40px}
.nav-links{position:absolute;left:520px;top:10px;display:flex;gap:31px;align-items:center;list-style:none}
.nav-links a{color:#fff;text-decoration:none;font-size:12.5px;font-weight:600}
.home-icon{width:14px;height:14px;display:block}
.login{position:absolute;left:1017px;top:2px;width:93px;height:36px;border-radius:18px;background:var(--blue);color:#fff;font-size:12.5px;font-weight:600;display:flex;align-items:center;justify-content:center;gap:6px}
.hero-title{left:75px;top:190px;font-size:52px;line-height:67px;color:#fff}
.hero-sub{left:75px;top:410px;width:360px;font-size:12.5px;line-height:19px;color:#fff}
.btn{display:inline-flex;align-items:center;justify-content:center;border-radius:20px;font-size:12px;font-weight:600;height:36px;padding:0 14px;white-space:nowrap}
.btn-pink{background:var(--pink);color:#fff}
.btn-ghost{border:1.5px solid var(--pink);color:var(--pink)}
.btn-blue{background:var(--blue);color:#fff}
.hero-cta{left:75px;top:472px;display:flex;gap:8px}
.brand-strip{top:583px;left:0;display:flex;gap:38px;align-items:center;white-space:nowrap;width:1200px;overflow:hidden}
.brand-strip span{font-size:24px;font-weight:500;color:rgba(255,255,255,.55);letter-spacing:.5px}

/* features */
.feat-title{left:159px;font-size:31px;line-height:46px}
.feat-rule{height:1px;background:var(--line)}
.feat{width:360px}
.feat .ico{position:absolute;left:0;top:-2px;width:62px;height:62px}
.feat h3{position:absolute;left:80px;top:0;font-size:12.5px;white-space:nowrap}
.feat p{position:absolute;left:81px;top:24px;width:275px;font-size:12.3px;line-height:19px;color:var(--muted)}
.feat a{position:absolute;left:81px;top:72px;font-size:12.3px;font-weight:600;color:var(--pink);text-decoration:none}
.dots{width:99px;height:58px;border-radius:4px;background:rgba(30,160,220,.16)}
.dots.on-dark{background:rgba(255,255,255,.14)}

/* why */
.why-title{top:1262px;text-align:center;font-size:31px;color:#fff}
.why-card{position:absolute;top:1379px;width:227px;height:212px;background:var(--card);border:1.5px solid #3c8db8;border-radius:3px;color:#fff}
.why-card.active{background:var(--blue);border-color:var(--blue)}
.why-card .badge{position:absolute;left:20px;top:-39px;width:78px;height:72px;border-radius:3px;display:flex;align-items:center;justify-content:center}
.why-card h3{position:absolute;left:20px;top:58px;width:190px;font-size:12px;line-height:19px}
.why-card p{position:absolute;left:20px;top:104px;width:190px;font-size:12.3px;line-height:19px;color:#eee}

/* testimonials */
.test-title{top:1818px;text-align:center;font-size:31px}
.t-card{position:absolute;top:1892px;width:256px;height:313px;border:1px solid #eee;border-radius:6px;background:#fff;box-shadow:0 2px 10px rgba(0,0,0,.04)}
.t-card .avatar{position:absolute;left:16px;top:18px;width:54px;height:54px;border-radius:50%;background:linear-gradient(135deg,#c9ccd0,#8d9297)}
.t-card h4{position:absolute;left:81px;top:31px;font-size:12.5px}
.t-card .role{position:absolute;left:81px;top:50px;font-size:7.5px;color:#555;white-space:nowrap}
.t-card blockquote{position:absolute;left:19px;top:94px;width:222px;font-size:12.2px;line-height:19px;color:#333}
.t-card .tag{position:absolute;left:22px;top:253px;font-size:15px;font-weight:500}
.t-card .stars{position:absolute;left:29px;top:279px;font-size:11px;color:var(--yellow);letter-spacing:1px}
.arrow{position:absolute;top:2041px;width:34px;height:34px;border-radius:50%;display:flex;align-items:center;justify-content:center;font-size:14px}
.arrow.prev{left:105px;border:1.5px solid var(--pink);color:var(--pink)}
.arrow.next{left:1061px;background:var(--pink);color:#fff}

/* news */
.news-title{top:2396px;text-align:center;font-size:31px;color:#fff}
.news-card{position:absolute;top:2459px;width:283px;height:296px;border-radius:8px;overflow:hidden}
.news-card .img{position:absolute;inset:0}
.news-card .img::after{content:"";position:absolute;inset:0;background:linear-gradient(180deg,rgba(0,0,0,0) 45%,rgba(0,0,0,.7) 100%)}
.news-card time{position:absolute;left:29px;top:219px;font-size:12px;color:#fff}
.news-card h3{position:absolute;left:29px;top:240px;width:240px;font-size:12.5px;line-height:19px;color:#fff}
.see-all{top:2792px;left:546px;height:34px;font-size:12px}

/* cta */
.cta-title{top:3000px;text-align:center;font-size:36px}
.cta-text{top:3066px;left:228px;width:744px;text-align:center;font-size:12.6px;line-height:19px;color:#333}
.cta-btns{top:3129px;left:0;width:1200px;display:flex;justify-content:center;gap:18px}
.cta-btns .btn{height:36px;padding:0 22px}

/* footer */
.f-logo{left:125px;top:3400px;font-size:62px;font-weight:300;color:#fff;letter-spacing:2px;line-height:66px}
.f-about{left:125px;top:3482px;width:255px;font-size:11px;line-height:17px;color:#fff}
.f-col h4{font-family:"Russo One",sans-serif;font-weight:400;font-size:13px;color:#fff;margin-bottom:14px}
.f-col ul{list-style:none}
.f-col li{font-size:10.5px;line-height:19px;color:#ddd}
.contact li{display:flex;gap:10px;align-items:flex-start;margin-bottom:12px;line-height:15px}
.contact svg{flex:none;margin-top:1px}
.f-sub p{font-size:10.5px;line-height:15px;color:#ddd;width:185px}
.f-email{margin-top:14px;width:178px;border-bottom:1px solid #777;font-size:8px;letter-spacing:2px;color:#aaa;padding:0 3px 6px}
.f-btn{margin-top:14px;margin-left:32px;height:32px;padding:0 20px;font-size:9.5px}
.f-rule{top:3574px;left:75px;width:1050px;height:1px;background:#555}
.copyright{top:3593px;text-align:center;font-family:"Russo One",sans-serif;font-size:9.5px;color:#fff}
.chat{left:1146px;top:3568px;width:32px;height:32px;border-radius:50%;background:var(--blue);display:flex;align-items:center;justify-content:center}
</style>
</head>
<body>

<div class="hero-photo" role="img" aria-label="Photo: a person at a desk working on code on a laptop screen in a bright office"></div>

<svg class="shapes" viewBox="0 0 1200 3623" aria-hidden="true">
  <polygon points="225,735 1200,625 1200,646 225,756" fill="var(--grey-band)"/>
  <polygon points="840,696 1200,643 1200,785" fill="var(--blue)"/>
  <polygon points="0,1218 1200,1140 1200,1653 0,1770" fill="var(--band)"/>
  <polygon points="0,2352 1200,2270 1200,2842 0,2903" fill="var(--blue)"/>
  <polygon points="360,3278 980,3228 980,3250 360,3300" fill="var(--grey-band)"/>
  <polygon points="0,3178 360,3300 0,3300" fill="var(--blue)"/>
  <polygon points="0,3328 1200,3252 1200,3623 0,3623" fill="var(--footer)"/>
</svg>

<header class="layer nav">
  <div class="logo">varplen.</div>
  <ul class="nav-links">
    <li><svg class="home-icon" viewBox="0 0 16 16"><path d="M8 1 1 7.5h2V15h4v-4h2v4h4V7.5h2z" fill="var(--blue)"/></svg></li>
    <li><a href="#">Features</a></li>
    <li><a href="#">Pricing</a></li>
    <li><a href="#">FAQ</a></li>
    <li><a href="#">About Us</a></li>
    <li><a href="#">News</a></li>
    <li><a href="#">Contact</a></li>
  </ul>
  <div class="login"><svg width="11" height="11" viewBox="0 0 12 12"><circle cx="6" cy="3.5" r="2.6" fill="#fff"/><path d="M1 12c0-3 2.2-5 5-5s5 2 5 5z" fill="#fff"/></svg>Log in</div>
</header>

<section style="top:0;height:720px">
  <h1 class="abs display hero-title">Manage Your<br>Events &amp; Courses<br>Effortlessly</h1>
  <p class="abs hero-sub">Trusted by Swedish organizations to handle registrations, payments, and communication — all in one place.</p>
  <div class="abs hero-cta"><span class="btn btn-pink">Book a Demo</span><span class="btn btn-ghost">Explore Features</span></div>
  <div class="abs brand-strip">
    <span style="margin-left:-8px">corvane</span><span>nexly</span><span>TARNOX</span><span>qubit</span><span>VELTRIX</span><span>Ombra</span><span>sellvia</span><span>halden</span><span>pyrra</span>
  </div>
</section>

<section style="top:800px;height:320px">
  <h2 class="abs display feat-title" style="top:52px">Everything You Need to<br>Organize Your Events</h2>
  <div class="abs feat-rule" style="top:164px;left:159px;width:385px"></div>
  <div class="abs feat-rule" style="top:164px;left:657px;width:385px"></div>

  <div class="abs feat" style="left:657px;top:52px;height:100px">
    <svg class="ico" viewBox="0 0 62 62" aria-hidden="true">
      <circle cx="38" cy="20" r="17" fill="var(--blue-soft)"/>
      <rect x="5" y="10" width="32" height="42" rx="2" fill="none" stroke="#1a1a1a" stroke-width="2"/>
      <rect x="11" y="16" width="10" height="10" fill="none" stroke="#1a1a1a" stroke-width="2"/>
      <path d="M25 18h7M25 23h7M11 32h20M11 38h20M11 44h12" stroke="#1a1a1a" stroke-width="2"/>
      <path d="M48 22 32 48l-2 6 5-4 16-26z" fill="#fff" stroke="#1a1a1a" stroke-width="2" stroke-linejoin="round"/>
    </svg>
    <h3 class="display">Registration &amp; Payments</h3>
    <p>Flexible forms, secure payments, group rates — everything you need for smooth sign-ups.</p>
    <a href="#">Learn More</a>
  </div>

  <div class="abs feat" style="left:157px;top:180px;height:100px">
    <svg class="ico" viewBox="0 0 62 62" aria-hidden="true">
      <circle cx="36" cy="18" r="17" fill="var(--blue-soft)"/>
      <path d="M22 10h30a5 5 0 0 1 5 5v14a5 5 0 0 1-5 5h-4v7l-8-7H22a5 5 0 0 1-5-5V15a5 5 0 0 1 5-5z" fill="#fff" stroke="#1a1a1a" stroke-width="2" stroke-linejoin="round"/>
      <path d="M25 18h24M25 24h18" stroke="#1a1a1a" stroke-width="2"/>
      <path d="M8 27h22a5 5 0 0 1 5 5v12a5 5 0 0 1-5 5H17l-8 7v-7a5 5 0 0 1-5-5V32a5 5 0 0 1 4-5z" fill="#fff" stroke="#1a1a1a" stroke-width="2" stroke-linejoin="round"/>
      <circle cx="13" cy="38" r="1.8" fill="#1a1a1a"/><circle cx="19" cy="38" r="1.8" fill="#1a1a1a"/><circle cx="25" cy="38" r="1.8" fill="#1a1a1a"/>
    </svg>
    <h3 class="display">Participant Communication</h3>
    <p>Send confirmations, reminders, and updates automatically with customizable templates.</p>
    <a href="#">Learn More</a>
  </div>

  <div class="abs feat" style="left:657px;top:180px;height:100px">
    <svg class="ico" viewBox="0 0 62 62" aria-hidden="true">
      <circle cx="38" cy="18" r="17" fill="var(--blue-soft)"/>
      <rect x="4" y="14" width="28" height="42" rx="2" fill="#fff" stroke="#1a1a1a" stroke-width="2"/>
      <rect x="9" y="8" width="30" height="42" rx="2" fill="#fff" stroke="#1a1a1a" stroke-width="2"/>
      <path d="M14 15h14M14 20h10" stroke="#1a1a1a" stroke-width="2"/>
      <path d="M15 44v-6M20 44v-10M25 44v-4M13 46h16" stroke="#1a1a1a" stroke-width="2"/>
      <circle cx="41" cy="30" r="10" fill="#fff" stroke="#1a1a1a" stroke-width="2"/>
      <path d="M41 20v10h10" fill="none" stroke="#1a1a1a" stroke-width="2"/>
    </svg>
    <h3 class="display">Reports &amp; Attendance</h3>
    <p>Export attendance lists, financial reports, and participant data in seconds.</p>
    <a href="#">Learn More</a>
  </div>
  <div class="abs dots" style="left:1024px;top:318px" role="img" aria-label="Decorative grid of small plus marks"></div>
</section>

<section style="top:0;height:1800px">
  <h2 class="abs display why-title" style="width:1200px">Why Choose Varplen</h2>
  <div class="why-card" style="left:125px">
    <div class="badge" style="background:var(--yellow)">
      <svg width="40" height="40" viewBox="0 0 40 40" aria-hidden="true"><path d="M20 5a11 11 0 0 0-6 20v5h12v-5a11 11 0 0 0-6-20z" fill="none" stroke="#fff" stroke-width="2.2" stroke-linejoin="round"/><path d="M15 34h10M17 38h6M20 30v-9M16 17l4 4 4-4" stroke="#fff" stroke-width="2.2" fill="none" stroke-linecap="round"/></svg>
    </div>
    <h3 class="display">Simple, intuitive interface</h3>
    <p>No complicated menus or clutter — Varplen is designed so anyone can easily manage registrations without extra training.</p>
  </div>
  <div class="why-card" style="left:366px">
    <div class="badge" style="background:var(--teal)">
      <svg width="40" height="40" viewBox="0 0 40 40" aria-hidden="true"><rect x="6" y="3" width="22" height="28" rx="2" fill="none" stroke="#fff" stroke-width="2.2"/><path d="M11 10h12M11 15h12M11 20h7" stroke="#fff" stroke-width="2.2"/><rect x="20" y="24" width="15" height="12" rx="2" fill="var(--teal)" stroke="#fff" stroke-width="2.2"/><path d="M23 24v-3a4.5 4.5 0 0 1 9 0v3" fill="none" stroke="#fff" stroke-width="2.2"/></svg>
    </div>
    <h3 class="display">Fully GDPR-compliant</h3>
    <p>Your participants' data is safe and handled according to all Swedish and EU privacy regulations.</p>
  </div>
  <div class="why-card active" style="left:608px">
    <div class="badge" style="background:var(--rose)">
      <svg width="44" height="40" viewBox="0 0 44 40" aria-hidden="true"><rect x="3" y="6" width="30" height="21" rx="2" fill="none" stroke="#fff" stroke-width="2.2"/><path d="M12 33h12M18 27v6" stroke="#fff" stroke-width="2.2"/><rect x="29" y="14" width="12" height="21" rx="2" fill="var(--rose)" stroke="#fff" stroke-width="2.2"/><circle cx="35" cy="31" r="1.3" fill="#fff"/></svg>
    </div>
    <h3 class="display">Responsive design for<br>all devices</h3>
    <p>Whether you're on a computer, tablet, or mobile, Varplen works seamlessly everywhere.</p>
  </div>
  <div class="why-card" style="left:848px">
    <div class="badge" style="background:var(--blue)">
      <svg width="40" height="40" viewBox="0 0 40 40" aria-hidden="true"><path d="M7 22v-4a13 13 0 0 1 26 0v4" fill="none" stroke="#fff" stroke-width="2.2"/><rect x="4" y="21" width="7" height="11" rx="2" fill="none" stroke="#fff" stroke-width="2.2"/><rect x="29" y="21" width="7" height="11" rx="2" fill="none" stroke="#fff" stroke-width="2.2"/><path d="M32 32c0 4-4 5-9 5" fill="none" stroke="#fff" stroke-width="2.2"/></svg>
    </div>
    <h3 class="display">Local support in Sweden</h3>
    <p>Get help from a friendly, knowledgeable team that understands your needs and speaks your language.</p>
  </div>
  <div class="abs dots on-dark" style="left:75px;top:1730px" role="img" aria-label="Decorative grid of small plus marks"></div>
</section>

<section style="top:0;height:2260px;pointer-events:none">
  <h2 class="abs display test-title" style="width:1200px">Testimonials</h2>
  <div class="arrow prev">‹</div>
  <div class="arrow next">›</div>
  <article class="t-card" style="left:201px">
    <div class="avatar" role="img" aria-label="Portrait photo of the reviewer"></div>
    <h4 class="display">Anders Holm</h4>
    <span class="role">Event Manager, Northway Business Forum</span>
    <blockquote>“Varplen has completely transformed the way we manage our events. The registration process is smooth, payments are secure, and our participants love the clear communication. We've saved hours of manual work every week.”</blockquote>
    <div class="tag">“Perfect Services”</div>
    <div class="stars">★★★★★</div>
  </article>
  <article class="t-card" style="left:473px">
    <div class="avatar" role="img" aria-label="Portrait photo of the reviewer"></div>
    <h4 class="display">Lina Berg</h4>
    <span class="role">Training Coordinator, Westbay Academy</span>
    <blockquote>“The automation tools are a game changer. Confirmation emails, reminders, and follow-ups happen without us lifting a finger. It's reliable, easy to use, and the support team is always quick to help.”</blockquote>
    <div class="tag">“Fastest Support”</div>
    <div class="stars">★★★★★</div>
  </article>
  <article class="t-card" style="left:744px">
    <div class="avatar" role="img" aria-label="Portrait photo of the reviewer"></div>
    <h4 class="display">Per Sandell,</h4>
    <span class="role">Sports Club Administrator</span>
    <blockquote>“Before Varplen, we struggled with messy spreadsheets and late payments. Now, everything is in one system and we can see live updates at any time. It's exactly what we needed.”</blockquote>
    <div class="tag">“Best Solutions</div>
    <div class="stars">★★★★★</div>
  </article>
  <div class="abs dots" style="left:1024px;top:2253px" role="img" aria-label="Decorative grid of small plus marks"></div>
</section>

<section style="top:0;height:2960px;pointer-events:none">
  <h2 class="abs display news-title" style="width:1200px">Latest from Varplen</h2>
  <article class="news-card" style="left:160px">
    <div class="img" role="img" aria-label="Photo: hands typing on a laptop showing an event screen" style="background:linear-gradient(135deg,#8a98a3,#3a444b)"></div>
    <time>July 12, 2025</time>
    <h3 class="display">How to Improve Your Event Registration Process</h3>
  </article>
  <article class="news-card" style="left:459px">
    <div class="img" role="img" aria-label="Photo: two colleagues reviewing a tablet together" style="background:linear-gradient(135deg,#d4d6d8,#3a4a66)"></div>
    <time>June 28, 2025</time>
    <h3 class="display">5 Tips for Effective Participant Communication</h3>
  </article>
  <article class="news-card" style="left:757px">
    <div class="img" role="img" aria-label="Photo: smiling man in a suit in an office" style="background:linear-gradient(135deg,#e0dbd3,#4a4541)"></div>
    <time>July 12, 2025</time>
    <h3 class="display">How to Improve Your Event Registration Process</h3>
  </article>
  <span class="abs btn btn-pink see-all">See All News</span>
  <div class="abs dots" style="left:75px;top:2865px;background:rgba(30,160,220,.2)" role="img" aria-label="Decorative grid of small plus marks"></div>
</section>

<section style="top:0;height:3200px;pointer-events:none">
  <h2 class="abs display cta-title" style="width:1200px">Ready to Simplify Your Event Management?</h2>
  <p class="abs cta-text">Take the stress out of registrations, payments, and participant communication. With Varplen, everything you need is in one easy-to-use platform — built for organizers like you.</p>
  <div class="abs cta-btns"><span class="btn btn-pink">Book a Demo</span><span class="btn btn-blue">large, centered</span></div>
</section>

<footer style="top:0;height:3623px;pointer-events:none">
  <div class="abs f-logo">varplen.</div>
  <p class="abs f-about">Lorem ipsum dolor sit amet, consectetur adipiscing elit, sed do eiusmod tempor incid idunt ut labore et dolore magna aliqua.</p>
  <div class="abs f-col" style="left:513px;top:3387px">
    <h4>QUICK LINKS</h4>
    <ul><li>Home</li><li>Firm Overview</li><li>Practice Areas</li><li>Verdicts &amp; Awards</li><li>Testimonials</li><li>Contact</li></ul>
  </div>
  <div class="abs f-col contact" style="left:682px;top:3387px">
    <h4>CONTACT US</h4>
    <ul>
      <li><svg width="11" height="11" viewBox="0 0 16 16"><path d="M3 1l3 1 1 4-2 1c1 2 2 3 4 4l1-2 4 1 1 3-2 2C7 15 1 9 1 3z" fill="#fff"/></svg>(+000) 555-0142</li>
      <li style="margin-top:6px"><svg width="11" height="11" viewBox="0 0 16 12"><rect x="0" y="0" width="16" height="12" rx="1" fill="#fff"/><path d="M0 1l8 6 8-6" stroke="#1f2429" stroke-width="1.5" fill="none"/></svg><span style="text-decoration:underline">info@varplen-example.se</span></li>
      <li style="margin-top:4px"><svg width="11" height="13" viewBox="0 0 12 16"><path d="M6 0a6 6 0 0 0-6 6c0 4 6 10 6 10s6-6 6-10a6 6 0 0 0-6-6zm0 8.5A2.5 2.5 0 1 1 6 3.5a2.5 2.5 0 0 1 0 5z" fill="#fff"/></svg>Lorem ipsum dolor sit<br>amet, consectetur adipiscing</li>
    </ul>
  </div>
  <div class="abs f-col f-sub" style="left:892px;top:3387px">
    <h4>SUBSCRIBE FOR UPDATES</h4>
    <p>Subscribe and be the first to receive all the latest insights.</p>
    <div class="f-email">EMAIL</div>
    <span class="btn btn-pink f-btn">SUBSCRIBE</span>
  </div>
  <div class="abs f-rule"></div>
  <p class="abs copyright" style="width:1200px">© 2025 COPYRIGHT VARPLEN, ALL RIGHTS RESERVED</p>
  <div class="abs chat"><svg width="16" height="14" viewBox="0 0 16 14" aria-hidden="true"><path d="M2 1h12a1.5 1.5 0 0 1 1.5 1.5v7A1.5 1.5 0 0 1 14 11H7l-4 3v-3H2A1.5 1.5 0 0 1 .5 9.5v-7A1.5 1.5 0 0 1 2 1z" fill="#fff"/></svg></div>
</footer>

</body>
</html>
```